Elegant invitation for prestigious fund raising event

Background
The Lanterns of Grace is a very prestigious fund raising event. It is a sit down dinner, gala type evening with a presentation and auction.
There are three of these event being held at venues around western North Carolina. The areas where these are being held all have one thing in common, they are in the Appalachian Mountains and the craft of quilt making. As you will see from the Concept Boards attached why a mountain theme and quilt “design feel” is being used. One very important point - we don’t want this design to look like an actual quilt.

See the concept board on page 4, which we can’t use that is from another artist but is one good interpretation of the idea and one way to stylize the picture with a “quilt” interpretation and feel. We do not want a literal quilt representation but are looking for an artistic way on how best to interpret what the quilt represents - the feel of “stitching together” the different things across our region that make us all unique but yet bind us all as one.

The Brief:
We want to develop an elegant invitation for these events.
We have develop as save the date (attached) and all we want to use of this is the wording “Lanterns of Grace” we do not like the icon above it.
Also attached is the wording for the invitation, along with the new picture we want to use (taken from the inspiration boards)

Size, fold, color and paper:

Around 5x7 inches, but open to any dimension if you have an idea that will work in a totally different size. Ideally try and stick to something that will fit a standard envelope so that we don’t need to make a special envelope

Fold – up to you if it has a fold or not and which way it folds. Our thought is that it will need a fold to keep it up market but open to any suggestions.
We are happy to print this on a textured paper if you have suggestions. It will be professionally digital printed so the paper needs to be suitable for digital printing

Color. The inspiration boards show the color palette. We have started out in the save the dates with the navy with reversed out white but again totally up to you to use anything from that color palette.
Updates

Target Market(s)

Up market, around 50 - 65 years old, many are retired, very wealthy

Industry/Entity Type

Event

Requirements
Must have
• See brief attached
Nice to have
• See brief attached
Should not have
• See brief attached

```html
<!DOCTYPE html>
<html lang="en">
<head>
<meta charset="UTF-8">
<title>Lanterns of Grace Invitation</title>
<link href="https://fonts.googleapis.com/css2?family=Fondamento:ital@1&display=swap" rel="stylesheet">
<style>
  :root {
    --backdrop: #000000;
    --card: #ffffff;
    --ink: #1b1b1b;
    --fold: #2a2a2a;
    --gold: #f9b93c;
    --gold-pale: #fde3a8;
  }
  * { margin: 0; padding: 0; box-sizing: border-box; }
  html, body {
    width: 1200px; height: 1200px; overflow: hidden;
    background: var(--backdrop);
  }
  .canvas { position: relative; width: 1200px; height: 1200px; }
  .card {
    position: absolute; left: 184px; top: 25px;
    width: 813px; height: 1155px;
    background: var(--card);
  }
  .fold-line {
    position: absolute; left: 0; top: 576px;
    width: 100%; height: 1px; background: var(--fold);
  }
  .copy {
    position: absolute; left: 0; width: 100%;
    text-align: center;
    font-family: "Fondamento", cursive;
    font-style: italic;
    font-size: 17px;
    line-height: 23px;
    color: var(--ink);
    white-space: nowrap;
  }
  .welcome { top: 218px; font-size: 15.5px; }
  .details { top: 719px; }
  .dress-code { top: 880px; }
  .beneficiary { top: 973px; }
  .ornament {
    position: absolute; width: 32px; height: 32px;
    background: var(--gold); opacity: 0.85; border-radius: 50%;
  }
  .ornament-band {
    position: absolute; left: 36px; width: 746px; height: 28px;
    background: var(--gold-pale); opacity: 0.7;
  }
</style>
</head>
<body>
<div class="canvas">
  <div class="card">
    <div class="ornament" style="left:130px; top:225px;" role="img" aria-label="Small golden six-petal flower ornament"></div>
    <div class="ornament" style="left:662px; top:225px;" role="img" aria-label="Small golden six-petal flower ornament"></div>
    <p class="copy welcome">
      You are invited to the Second annual Lanterns of Grace on the plateau.<br>
      Please join us for an elegant and entertaining affair benefiting the<br>
      healthcare in our region.
    </p>

    <div class="fold-line"></div>

    <div class="ornament-band" style="top:604px;" role="img" aria-label="Row of pale golden six-petal flower ornaments"></div>

    <p class="copy details">
      6th of June, 2016<br>
      The Meadow at Old Harwick Inn<br>
      Beginning at 5:30pm<br>
      Valet Parking
    </p>

    <div class="ornament" style="left:390px; top:823px;" role="img" aria-label="Small golden six-petal flower ornament"></div>

    <p class="copy dress-code">Cockatil Attire &nbsp;|&nbsp; Valet Parking</p>

    <div class="ornament" style="left:390px; top:921px;" role="img" aria-label="Small golden six-petal flower ornament"></div>

    <p class="copy beneficiary">
      All proceeds from the night will go to benefit<br>
      Ridgeview Valley Hospital
    </p>

    <div class="ornament-band" style="top:1101px;" role="img" aria-label="Row of pale golden six-petal flower ornaments"></div>
  </div>
</div>
</body>
</html>
```